Super-fantastic-interesting infographic of terribly boring content

-Looking to provide a visually engaging snapshot of the average Canadian investor.
-Help people compare their personal financial situation against the infographic (Average).
-We want viewers to feel engaged and interested in the info presented, not confused and irritated.

Data points to present:

The average Canadian snapshot:
* Average Canadian household Income in 2016: $76,900
* Median Net Worth of Canadian families in 2016: $295,100
* Average annual household expenditures on goods a& services: $62,183
* Median value in principal residence: $349,000
* Highest net annual savings amount (Age 35-44): $10,120
* Number of Canadian families holding a mortgage: 38.4%
* Median Mortgage value of Principal residence: $190,000
* Debt to disposable income ratio average: 172.1
* Total value of all assets held by Canadians in 2016: 12 Trillion dollars
* The principal residence was the single largest asset held (of the 12 Trillion): 32%
* Private pensions was the 2nd largest grouping of assets at 29.2%
* The average borrowing rate for Canadian mortgages: 2.94%
* 74% were fixed rate, 21% were variable and 5% blended.
* 48% of Canadians do not save or invest at all
* 54% of Canadians do not budget regularly
* 1 in 3 Canadians have lost at least 20% in one year
* 51% of Canadians took NO ACTION after losing at least 20% in one year.
* 22% of those people either, hired or fired an advisor

Financial advice landscape:
* # of households in Canada: 13,300,000
* Households with an advisor 5,300,000
* % of households dissatisfied with existing advisor 1,100,000

Target Market(s)

Investors, ages 22-55

Industry/Entity Type

Financial

Font styles to use
Sans Serif

Colors

Designer to choose colors to be used in the design.

Requirements
Must have
• Header: Financial landscape of the average Canadian
Nice to have
• There is a lot of numbers and percentages, find a way to deliver the info using a mix of images, numbers, pictures etc.

```html
<!DOCTYPE html>
<html lang="en">
<head>
<meta charset="utf-8">
<title>The Average Canadian Snapshot</title>
<link href="https://fonts.googleapis.com/css2?family=Anton&family=Oswald:wght@400;500;600;700&family=Lilita+One&display=swap" rel="stylesheet">
<style>
:root{
  --red:#e3414a;
  --red-deep:#a3161c;
  --pink:#f29a9a;
  --pink-soft:#f7c3c1;
  --blush:#fbe3e1;
  --ink:#161616;
  --white:#ffffff;
  --teal:#8fd0cc;
  --teal-soft:#86cbc6;
  --green:#7fc99a;
  --blue:#1414e6;
  --yellow:#ffe23a;
  --orange:#ff6a00;
  --bar-blue:#3c5aa6;
  --gold:#e6a21a;
}
*{margin:0;padding:0;box-sizing:border-box}
html,body{width:1200px;height:3000px;overflow:hidden}
body{position:relative;background:var(--white);font-family:"Oswald",sans-serif;color:var(--ink)}
.abs{position:absolute}
.band{position:absolute;left:0;width:1200px}

/* header */
.title-band{top:0;height:120px;background:var(--red)}
.title{top:12px;left:0;width:1200px;text-align:center;font-family:"Anton",sans-serif;font-size:86px;line-height:96px;color:var(--ink);letter-spacing:1px}
.snapshot-band{top:120px;height:370px;background:linear-gradient(180deg,var(--pink-soft),var(--blush))}
.hand-art{left:0;top:140px;width:200px;height:130px;background:linear-gradient(135deg,#f0b27a,#2a2a2a);border-radius:0 70px 70px 0}
.coin{width:56px;height:56px;border-radius:50%;background:var(--gold);border:5px solid #c98200}
.tag{font-family:"Lilita One",sans-serif;font-size:52px;line-height:60px;color:var(--yellow);-webkit-text-stroke:3px var(--ink);letter-spacing:2px}
.stat-label{text-align:right;font-size:28px;line-height:29px;font-weight:500}
.meter{width:200px;height:42px;border:3px solid var(--ink);background:var(--white);border-radius:8px;box-shadow:3px 3px 0 #6a6a6a}
.meter i{display:block;height:100%;border-radius:4px 0 0 4px}
.big-val{font-family:"Anton",sans-serif;font-size:56px;line-height:66px;color:var(--red-deep)}

/* family */
.family-band{top:560px;height:280px;background:var(--pink)}
.h-sec{font-family:"Anton",sans-serif;font-size:62px;line-height:74px;color:var(--ink);letter-spacing:1px}
.family-art{left:830px;top:500px;width:330px;height:340px;border-radius:160px 160px 20px 20px;background:linear-gradient(160deg,#e9875a,#6d9f3f 60%,#3a5d9a)}
.line{font-size:32px;line-height:56px;font-weight:500;white-space:nowrap}
.line b{font-family:"Anton",sans-serif;font-weight:400;font-size:50px;color:var(--red-deep)}
.small-note{font-size:20px;line-height:22px;font-weight:600}

/* assets */
.trillion{left:300px;top:900px;width:600px;text-align:center;font-family:"Anton",sans-serif;font-size:56px;line-height:68px;color:var(--red-deep)}
.trillion-sub{left:300px;top:970px;width:600px;text-align:center;font-size:28px;line-height:36px;font-weight:600;background:var(--yellow)}
.rank{font-family:"Anton",sans-serif;font-size:62px;line-height:64px}
.rank-sub{font-size:27px;line-height:36px;font-weight:600;background:var(--yellow);padding:0 6px}
.blob{border-radius:50%;background:var(--teal-soft)}
.pct-disc{border-radius:50%;background:var(--green);display:flex;align-items:center;justify-content:center;font-family:"Anton",sans-serif;font-size:60px;color:var(--red-deep)}
.asset-name{font-family:"Anton",sans-serif;font-size:46px;line-height:58px;text-align:center;color:var(--ink)}
.frame{border:18px solid var(--teal);background:var(--white)}
.frame.rounded{border-radius:18px}
.blue-label{color:var(--blue);font-size:31px;line-height:36px}
.plain-label{font-size:32px;line-height:50px;white-space:nowrap}
.val-red{font-family:"Anton",sans-serif;font-size:44px;color:var(--red-deep)}
.pct-row{display:flex;align-items:center;gap:16px}
.huge-pct{font-family:"Anton",sans-serif;font-size:80px;line-height:90px;color:var(--red-deep);white-space:nowrap}
.note{font-size:28px;line-height:31px}
.note em{font-style:normal;color:var(--blue)}
.art{display:block}

/* debt */
.debt-band{top:1720px;height:270px;background:var(--pink)}
.debt-title{font-size:32px;line-height:48px;font-weight:500;white-space:nowrap}
.debt-title span{color:var(--blue)}
.debt-title b{font-family:"Anton",sans-serif;font-weight:400;font-size:38px;color:var(--red-deep);margin-left:10px}
.borrow-h{font-size:18px;line-height:22px}
.borrow-row{font-size:24px;line-height:32px;font-weight:600;color:#333}
.borrow-bar{height:28px;background:var(--teal)}
.borrow-pct{font-size:22px;line-height:32px;font-weight:600;color:#333}
.debt-art{left:870px;top:1700px;width:290px;height:280px;background:linear-gradient(200deg,#f0b27a,#d94452 55%,#3a6fb0);border-radius:30px}

/* loss */
.loss-text{font-size:32px;line-height:80px;white-space:nowrap}
.loss-text b{font-family:"Anton",sans-serif;font-weight:400;color:var(--blue);font-size:64px}
.loss-text strong{font-family:"Anton",sans-serif;font-weight:400;color:var(--red-deep);font-size:64px}
.divider{left:480px;top:2050px;width:2px;height:300px;background:var(--pink)}
.action{font-size:30px;line-height:36px;white-space:nowrap}
.action b{font-family:"Anton",sans-serif;font-weight:400;color:var(--blue);font-size:56px;line-height:60px}
.action em{font-style:normal;color:var(--blue);font-weight:600}

/* advice */
.advice-band{top:2370px;height:550px;background:var(--pink)}
.map-art{left:580px;top:2400px;width:600px;height:440px;background:radial-gradient(ellipse at 60% 55%,#d91e2a,#ec5860 65%,rgba(242,154,154,0) 100%)}
.advisor-art{left:0;top:2420px;width:400px;height:580px;background:linear-gradient(180deg,#e8a77a 0 20%,#1a1a1a 20% 100%);border-radius:180px 180px 0 0}
.advice-h{font-family:"Anton",sans-serif;font-size:64px;line-height:76px;color:var(--ink)}
.adv-label{font-size:31px;line-height:40px;text-align:right;font-weight:500}
.adv-val{font-family:"Anton",sans-serif;font-size:44px;line-height:56px;color:var(--white);-webkit-text-stroke:2px var(--ink);letter-spacing:1px}
.adv-val.blue{color:var(--blue);-webkit-text-stroke:0}
.foot-band{top:2920px;height:80px;background:var(--red)}
.brand{left:840px;top:2940px;font-size:26px;line-height:40px;font-weight:600;color:var(--ink);display:flex;align-items:center;gap:14px}
.brand i{width:40px;height:40px;border-radius:50%;background:var(--white)}
</style>
</head>
<body>

<!-- Header -->
<div class="band title-band"></div>
<h1 class="abs title">THE AVERAGE CANADIAN SNAPSHOT</h1>

<!-- Income / expenses / savings -->
<div class="band snapshot-band"></div>
<div class="abs hand-art" role="img" aria-label="Illustration of a hand dropping a gold coin"></div>
<div class="abs coin" style="left:150px;top:272px"></div>
<div class="abs coin" style="left:125px;top:380px"></div>

<div class="abs tag" style="left:228px;top:166px">INCOME</div>
<div class="abs tag" style="left:220px;top:272px">EXPENSES</div>
<div class="abs tag" style="left:222px;top:384px">SAVINGS</div>

<div class="abs stat-label" style="left:470px;top:186px;width:290px">Household income</div>
<div class="abs stat-label" style="left:470px;top:250px;width:290px">Average annual household expenditure on goods &amp; services:</div>
<div class="abs stat-label" style="left:470px;top:380px;width:290px">Highest net annual savings amount (age 35-44)</div>

<div class="abs meter" style="left:778px;top:174px"><i style="width:86%;background:var(--bar-blue)"></i></div>
<div class="abs meter" style="left:778px;top:276px"><i style="width:72%;background:var(--orange)"></i></div>
<div class="abs meter" style="left:778px;top:394px"><i style="width:12%;background:var(--yellow)"></i></div>

<div class="abs big-val" style="left:990px;top:160px">$76,900</div>
<div class="abs big-val" style="left:990px;top:262px">$62,183</div>
<div class="abs big-val" style="left:990px;top:380px">$10,120</div>

<!-- Canadian family -->
<div class="band family-band"></div>
<div class="abs family-art" role="img" aria-label="Illustration of a smiling family of four"></div>
<div class="abs h-sec" style="left:24px;top:566px">CANADIAN FAMILY</div>
<div class="abs line" style="left:24px;top:638px">Median Net Worth of Canadian families : <b>$295,100</b></div>
<div class="abs small-note" style="left:24px;top:696px">(in 2016)</div>
<div class="abs line" style="left:24px;top:732px">Numbers of Canadian families holding a mortgage : <b>38.4%</b></div>

<!-- 12 trillion burst and arrows -->
<svg class="abs art" style="left:0;top:780px" width="1200" height="320" viewBox="0 0 1200 320">
  <polygon fill="#ffe23a" stroke="#161616" stroke-width="3"
    points="600,10 640,90 720,30 705,105 820,70 775,140 880,150 790,190 850,250 740,220 720,300 660,230 600,310 560,230 480,290 480,215 370,240 430,180 320,150 420,130 380,60 490,100 500,20 560,90"/>
  <path d="M390,180 C260,160 180,200 170,270" fill="none" stroke="#c0151e" stroke-width="34"/>
  <polygon points="130,250 215,250 172,320" fill="#c0151e"/>
  <path d="M810,180 C930,160 1000,190 1020,250" fill="none" stroke="#c0151e" stroke-width="34"/>
  <polygon points="980,240 1065,230 1035,300" fill="#c0151e"/>
</svg>
<div class="abs trillion">12 Trillion dollars</div>
<div class="abs trillion-sub">Total value of all assets held by canadians</div>

<!-- Principal residence -->
<div class="abs frame rounded" style="left:40px;top:1160px;width:555px;height:545px"></div>
<div class="abs blob" style="left:64px;top:1058px;width:330px;height:330px"></div>
<div class="abs rank" style="left:60px;top:1040px">1st</div>
<div class="abs rank-sub" style="left:20px;top:1106px">Largest assets</div>
<div class="abs asset-name" style="left:90px;top:1160px;width:280px">PRINCIPAL<br>RESIDENCE</div>
<div class="abs pct-disc" style="left:330px;top:1125px;width:160px;height:160px">32%</div>
<div class="abs" role="img" aria-label="Illustration of a small house" style="left:130px;top:1290px;width:200px;height:105px;background:linear-gradient(180deg,#8a5a3c 0 38%,#e2c79a 38% 100%);border-radius:6px"></div>
<div class="abs blue-label" style="left:72px;top:1428px">Median value</div>
<div class="abs plain-label" style="left:72px;top:1460px">in principle residence : <span class="val-red">$349,000</span></div>
<div class="abs blue-label" style="left:72px;top:1538px">Median Mortgage value</div>
<div class="abs plain-label" style="left:72px;top:1570px">of principle residence : <span class="val-red">$190,000</span></div>

<!-- Private pensions -->
<div class="abs blob" style="left:790px;top:990px;width:370px;height:370px"></div>
<div class="abs" role="img" aria-label="Illustration of an elderly couple with walking canes" style="left:680px;top:1045px;width:130px;height:225px;background:linear-gradient(180deg,#e6e6e6 0 20%,#e57a3a 20% 55%,#4a5fa0 55% 100%);border-radius:60px 60px 8px 8px"></div>
<div class="abs rank" style="left:968px;top:980px">2nd</div>
<div class="abs rank-sub" style="left:935px;top:1040px">Largest assets</div>
<div class="abs asset-name" style="left:820px;top:1082px;width:210px">PRIVATE<br>PENSIONS</div>
<div class="abs pct-disc" style="left:1016px;top:1130px;width:150px;height:150px;font-size:48px">29.2%</div>

<div class="abs frame" style="left:630px;top:1290px;width:545px;height:200px;border-width:16px"></div>
<div class="abs pct-row" style="left:726px;top:1306px;height:168px">
  <div class="huge-pct">48%</div>
  <div class="note">Canadian<br><em>DO NOT SAVE or INVEST</em><br>at all</div>
</div>

<div class="abs frame" style="left:630px;top:1510px;width:545px;height:200px;border-width:16px"></div>
<div class="abs pct-row" style="left:742px;top:1526px;height:168px">
  <div class="huge-pct">54%</div>
  <div class="note">Canadian<br><em>DO NOTBUDGET</em><br>regularly</div>
</div>

<!-- Debt -->
<div class="band debt-band"></div>
<div class="abs debt-art" role="img" aria-label="Illustration of a frustrated man holding a red arrow sign reading DEBTS"></div>
<div class="abs debt-title" style="left:40px;top:1740px"><span>Debt</span> to Disposable income ratio average : <b>172.1</b></div>
<div class="abs borrow-h" style="left:40px;top:1800px">Type of Borrowing</div>
<div class="abs borrow-row" style="left:40px;top:1824px">Flexible Rate</div>
<div class="abs borrow-bar" style="left:192px;top:1826px;width:354px"></div>
<div class="abs borrow-pct" style="left:552px;top:1824px">74%</div>
<div class="abs borrow-row" style="left:62px;top:1862px">Variable</div>
<div class="abs borrow-bar" style="left:192px;top:1864px;width:76px"></div>
<div class="abs borrow-pct" style="left:274px;top:1862px">21%</div>
<div class="abs borrow-row" style="left:62px;top:1900px">Blended</div>
<div class="abs borrow-bar" style="left:192px;top:1902px;width:14px"></div>
<div class="abs borrow-pct" style="left:214px;top:1900px">5%</div>
<div class="abs debt-title" style="left:40px;top:1944px">The average <span>borrowing rate</span> for Canadian mortgages : <b>2.94%</b></div>

<!-- Losses -->
<svg class="abs art" style="left:95px;top:2050px" width="240" height="180" viewBox="0 0 240 180">
  <g fill="#86cbc6"><circle cx="35" cy="18" r="16"/><rect x="12" y="40" width="46" height="70" rx="10"/><rect x="16" y="100" width="16" height="72" rx="6"/><rect x="38" y="100" width="16" height="72" rx="6"/></g>
  <g fill="#8a8a8a"><circle cx="110" cy="18" r="16"/><rect x="87" y="40" width="46" height="70" rx="10"/><rect x="91" y="100" width="16" height="72" rx="6"/><rect x="113" y="100" width="16" height="72" rx="6"/></g>
  <g fill="#8a8a8a"><circle cx="185" cy="18" r="16"/><rect x="162" y="40" width="46" height="70" rx="10"/><rect x="166" y="100" width="16" height="72" rx="6"/><rect x="188" y="100" width="16" height="72" rx="6"/></g>
</svg>
<div class="abs loss-text" style="left:50px;top:2180px">1 in 3 Canadians have <b>LOST</b></div>
<div class="abs loss-text" style="left:50px;top:2260px">at least <strong>20%</strong> in one year</div>

<div class="abs divider"></div>

<svg class="abs art" style="left:515px;top:2000px" width="170" height="170" viewBox="0 0 170 170">
  <circle cx="85" cy="85" r="60" fill="none" stroke="#8a8a8a" stroke-width="50"/>
  <circle cx="85" cy="85" r="60" fill="none" stroke="#7cc230" stroke-width="50"
    stroke-dasharray="192.3 377" transform="rotate(-90 85 85)"/>
</svg>
<div class="abs pct-row" style="left:566px;top:2062px">
  <div class="huge-pct" style="font-size:70px;line-height:80px">51%</div>
  <div class="action"><b>NO ACTION</b> <span style="display:none"></span></div>
</div>
<div class="abs action" style="left:682px;top:2062px;display:none"></div>
<div class="abs pct-row" style="left:566px;top:2220px">
  <div class="huge-pct" style="font-size:72px;line-height:82px">22%</div>
  <div class="action">of those people either<br><em>HIRED, or FIRED</em> an advisor.</div>
</div>

<!-- Financial advice landscape -->
<div class="band advice-band"></div>
<div class="abs map-art" role="img" aria-label="Red map of Canada"></div>
<div class="abs advisor-art" role="img" aria-label="Illustration of a businessman in a suit holding a blue folder"></div>
<div class="abs advice-h" style="left:368px;top:2404px">FINANCIAL ADVICE LANDSCAPE</div>

<div class="abs adv-label" style="left:430px;top:2546px;width:340px">Number of households :</div>
<div class="abs adv-val" style="left:786px;top:2538px">13,300,000</div>

<div class="abs adv-label" style="left:430px;top:2642px;width:340px">Households with advisors :</div>
<div class="abs adv-val" style="left:786px;top:2634px">5,300,000 (38%)</div>

<div class="abs adv-label" style="left:410px;top:2736px;width:360px">Households <span style="color:var(--blue)">dissatisfied</span> with<br>existing advisors :</div>
<div class="abs adv-val blue" style="left:790px;top:2766px">1,100,000 (20.7%)</div>

<div class="band foot-band"></div>
<div class="abs brand"><span style="font-size:18px">By</span><i></i><span>NorthLedger</span></div>

</body>
</html>
```